TRENDY & MODERN BUSINESS CARD DESIGN for Media Company *

I need a minimalistic - clean - modern and professional business card layout and design for MEDIA & PHOTOGRAPHY STUDIO.

We do NOT have a logo, and not really looking for one - but rather excellent typography and design. We would consider the 3 as a focal point.

We do personal and commercial photography.

Target Market(s)

Personal and commercial photography clientele

Contact Information for Business Card

ZUB size - from zub.com / size guidelines are enclosed in the brief

Font styles to use
Sans Serif

Colors
f78f20
eda3c7
cee9f5
0555a3
e667a6
fbf289

Requirements
Must have
• Clean lines - Modern layout
Nice to have
• All blue background as an option - use color palette in brief please.
Should not have
• Old fashion fonts and regular fonts.

```html
<!DOCTYPE html>
<html lang="en">
<head>
<meta charset="utf-8">
<title>Northlight Media – Business Card</title>
<link rel="stylesheet" href="https://fonts.googleapis.com/css2?family=Roboto:wght@400;500;700&family=Roboto+Condensed:wght@400&family=Open+Sans:wght@400&display=swap">
<style>
  :root {
    --backdrop: #5b5b5b;
    --card-light: #f3f3f3;
    --card-dark: #2b2b2b;
    --pink: #e667a6;
    --yellow: #fbf289;
    --red: #ee1c24;
    --ink: #3a3a3a;
    --muted: #6b6b6b;
    --white: #ffffff;
  }
  * { margin: 0; padding: 0; box-sizing: border-box; }
  html, body {
    width: 1200px; height: 900px; overflow: hidden;
    background: var(--backdrop);
    font-family: "Open Sans", Arial, sans-serif;
  }
  .stage { position: relative; width: 1200px; height: 900px; }

  .card {
    position: absolute; top: 200px;
    width: 310px; height: 502px;
  }
  .card--front {
    left: 253px; background: var(--card-light);
    border-radius: 62px 0 62px 0;
  }
  .card--back {
    left: 627px; background: var(--card-dark);
    border-radius: 0 62px 0 62px;
  }

  .brand-dot {
    position: absolute; left: 129px; top: 88px;
    width: 52px; height: 52px; border-radius: 50%;
    background: var(--pink);
  }
  .brand-name {
    position: absolute; left: 0; right: 0; top: 201px;
    text-align: center;
    font-family: "Roboto Condensed", "Roboto", sans-serif;
    font-weight: 400;
    font-size: 29px; color: var(--ink); letter-spacing: 0.3px;
  }
  .tagline {
    position: absolute; left: 0; right: 0; top: 236px;
    text-align: center;
    font-family: "Roboto", sans-serif;
    font-size: 9px; letter-spacing: 2.6px; color: var(--muted);
  }

  .contact { position: absolute; left: 34px; top: 319px; }
  .contact__name {
    font-family: "Roboto", sans-serif; font-weight: 700;
    font-size: 17px; color: var(--pink); line-height: 22px;
  }
  .contact__role { font-size: 14px; color: var(--red); line-height: 19px; }
  .contact__lines { margin-top: 10px; font-size: 14px; color: var(--ink); line-height: 18px; }
  .contact__line { display: flex; align-items: center; gap: 4px; }
  .contact__line svg { width: 13px; height: 11px; fill: var(--pink); }
  .contact__address { margin-top: 13px; font-size: 14px; color: var(--ink); line-height: 17px; }

  .back-name {
    position: absolute; left: 0; right: 0; top: 205px;
    text-align: center;
    font-family: "Roboto Condensed", "Roboto", sans-serif;
    font-weight: 400;
    font-size: 30px; color: var(--yellow);
  }
  .cities {
    position: absolute; left: 42px; top: 345px;
    list-style: none;
    font-family: "Roboto", sans-serif; font-size: 14px;
    color: var(--white); line-height: 22.7px;
  }
  .cities li { display: flex; align-items: center; gap: 5px; }
  .cities li::before {
    content: ""; width: 7px; height: 7px; border-radius: 50%;
    background: var(--red);
  }
</style>
</head>
<body>
<main class="stage">
  <section class="card card--front">
    <span class="brand-dot"></span>
    <h1 class="brand-name">NORTHLIGHT MEDIA</h1>
    <p class="tagline">FRAMING LIGHT.&nbsp; MAKING STORIES</p>

    <div class="contact">
      <h2 class="contact__name">MARISOL VEGA</h2>
      <p class="contact__role">Founder &amp; Media Director</p>
      <div class="contact__lines">
        <p class="contact__line">
          <svg viewBox="0 0 13 11" aria-hidden="true"><path d="M1 3.5C1 2 3 1 6.5 1S12 2 12 3.5V5H9V3.8H4V5H1Z"/><rect x="2.5" y="6" width="8" height="4.5" rx="1"/></svg>
          (305) 555-0148
        </p>
        <p class="contact__line">
          <svg viewBox="0 0 13 11" aria-hidden="true"><path d="M0.5 1.5h12v8h-12z M1.5 2.5l5 3.6 5-3.6" stroke="#f3f3f3" stroke-width="0.9"/></svg>
          marisol@northlightmedia.com
        </p>
      </div>
      <p class="contact__address">2400 Harbor Avenue<br>6th Floor,Bayview, FL 30210</p>
    </div>
  </section>

  <section class="card card--back">
    <p class="back-name">NORTHLIGHT</p>
    <ul class="cities">
      <li>MIAMI</li>
      <li>NEW YORK</li>
      <li>LAS VEGAS</li>
      <li>CANCUN</li>
      <li>ROMA</li>
    </ul>
  </section>
</main>
</body>
</html>
```